Land Buying Company Needs Letterhead for Direct Mail Marketing to Land Owners

We are looking for a professional letterhead that we will be including in our direct mail marketing. We will be sending this to land owners who may be interested in selling or purchasing land.

The letterhead needs to be editable. Headers and footers would look nice, but we are open. We would want it to include our address, website, phone, and email info. For right now the address to use for design purposes would the following:

Address: 415 Bramwell Avenue #600
Dallas, TX 75219
Website - www.quillridgeacres.example
Email - info@quillridgeacres.example
Phone - 866-402-ACRE

I have attached our logo zip file that we just had done on Pixel Guild. Let me know what questions you have, and thank you.

```html
<!DOCTYPE html>
<html lang="en">
<head>
<meta charset="utf-8">
<title>Quill Ridge Acres – Letterhead</title>
<link rel="stylesheet" href="https://fonts.googleapis.com/css2?family=Montserrat:wght@500;700;800&family=Open+Sans:ital,wght@0,300;0,400;0,700;1,300&display=swap">
<style>
  :root {
    --canvas: #f1f1f1;
    --paper: #e9e9e8;
    --forest: #455d2b;
    --leaf: #8dc63f;
    --ink: #2b2b2b;
    --body-ink: #444;
    --rule: #5d7a34;
    --faint-circle: #d4d4cf;
    --moon: #6d7a53;
    --signature-tone: #dcdcda;
    --white: #ffffff;
  }
  * { box-sizing: border-box; margin: 0; padding: 0; }
  html, body { width: 1200px; height: 1200px; overflow: hidden; }
  body {
    background: var(--canvas);
    position: relative;
    font-family: "Open Sans", Arial, sans-serif;
    color: var(--ink);
  }

  .sheet { position: absolute; overflow: hidden; }

  /* Front: the letter */
  .letter {
    left: 81px; top: 241px; width: 488px; height: 684px;
    background: var(--paper);
  }
  .letter__backdrop {
    position: absolute; left: 88px; top: 190px;
    width: 312px; height: 312px; border-radius: 50%;
    background: var(--faint-circle);
  }
  .letter__header {
    position: absolute; left: 0; top: 0; width: 100%; height: 89px;
    border-bottom: 1.5px solid var(--rule);
  }
  .brand {
    position: absolute; display: flex; align-items: center; gap: 7px;
  }
  .brand__dot { border-radius: 50%; background: var(--forest); flex: none; }
  .brand__name {
    font-family: "Montserrat", Arial, sans-serif; font-weight: 800;
    color: var(--leaf); letter-spacing: 0.3px; white-space: nowrap;
  }
  .letter .brand { left: 44px; top: 44px; }
  .letter .brand__dot { width: 30px; height: 30px; }
  .letter .brand__name { font-size: 12.5px; }

  .contact { position: absolute; left: 266px; top: 34px; list-style: none; }
  .contact li {
    display: flex; align-items: center; gap: 8px;
    font-size: 11px; line-height: 15px; color: var(--ink);
  }
  .contact svg { width: 9px; height: 9px; fill: var(--forest); flex: none; }
  .contact .web { color: var(--leaf); }

  .letter__content { position: absolute; left: 46px; top: 133px; width: 404px; }
  .date { font-size: 15px; }
  .recipient { font-size: 15px; margin-top: 12px; }
  .address { font-size: 18px; font-weight: 300; line-height: 22px; margin-top: 18px; }
  .salutation { font-size: 17px; font-weight: 700; margin-top: 10px; }
  .body-copy {
    font-size: 15.5px; font-weight: 300; line-height: 19.6px;
    text-align: justify; color: var(--body-ink); margin-top: 14px;
    hyphens: auto;
  }
  .closing {
    position: absolute; left: 56px; top: 487px;
    font-size: 16.5px; font-weight: 300; font-style: italic;
  }
  .signature {
    position: absolute; left: 42px; top: 526px; width: 210px; height: 58px;
    border-radius: 4px;
    background: linear-gradient(90deg, var(--signature-tone), rgba(220,220,218,0));
  }

  .letter__footer {
    position: absolute; left: 0; bottom: 0; width: 100%; height: 33px;
    background: var(--forest); color: var(--white);
    display: flex; align-items: center; justify-content: center; gap: 14px;
    font-size: 13px;
  }
  .letter__footer svg { width: 12px; height: 16px; fill: var(--white); }

  /* Back: cover */
  .cover {
    left: 637px; top: 237px; width: 486px; height: 691px;
    background: var(--forest);
  }
  .cover__moon {
    position: absolute; left: 71px; top: 196px;
    width: 358px; height: 358px; border-radius: 50%;
    background: var(--moon);
  }
  .cover .brand { left: 134px; top: 323px; gap: 9px; }
  .cover .brand__dot { width: 38px; height: 38px; background: var(--white); }
  .cover .brand__name { font-size: 18px; }
</style>
</head>
<body>

  <section class="sheet letter">
    <div class="letter__backdrop"></div>

    <header class="letter__header">
      <div class="brand">
        <span class="brand__dot"></span>
        <span class="brand__name">QUILL RIDGE ACRES</span>
      </div>
      <ul class="contact">
        <li>
          <svg viewBox="0 0 24 24"><path d="M6.6 10.8a15 15 0 0 0 6.6 6.6l2.2-2.2c.3-.3.7-.4 1-.2 1.1.4 2.3.6 3.6.6.6 0 1 .4 1 1V20c0 .6-.4 1-1 1A17 17 0 0 1 3 4c0-.6.4-1 1-1h3.5c.6 0 1 .4 1 1 0 1.3.2 2.5.6 3.6.1.3 0 .7-.2 1z"/></svg>
          866-402-ACRE
        </li>
        <li>
          <svg viewBox="0 0 24 24"><path d="M2 5h20v14H2z"/></svg>
          info@quillridgeacres.example
        </li>
        <li>
          <svg viewBox="0 0 24 24"><circle cx="12" cy="12" r="10"/></svg>
          <span class="web">www.quillridgeacres.example</span>
        </li>
      </ul>
    </header>

    <main class="letter__content">
      <p class="date">Aug 16-2020</p>
      <p class="recipient">MR Alan Merrow</p>
      <p class="address">27 Fieldstone Ln<br>Millbrook, NJ 08510</p>
      <p class="salutation">Dear Alan</p>
      <p class="body-copy">The standard chunk of Lorem Ipsum used since the 1500s is reproduced below for those interested. Sections 1.10.32 and 1.10.33 from "de Finibus Bonorum et Malorum" by Varro Lentus are also reproduced in their exact original form, accompanied by English versions from the 1914 translation by J. Pemberly</p>
    </main>

    <p class="closing">Yours faithfully</p>
    <div class="signature" role="img" aria-label="Handwritten signature of the sender"></div>

    <footer class="letter__footer">
      <svg viewBox="0 0 12 16"><path d="M6 0a6 6 0 0 0-6 6c0 4.5 6 10 6 10s6-5.5 6-10a6 6 0 0 0-6-6zm0 8.5A2.5 2.5 0 1 1 6 3.5a2.5 2.5 0 0 1 0 5z"/></svg>
      <span>415 Bramwell Avenue #600 Dallas, TX 75219</span>
    </footer>
  </section>

  <section class="sheet cover">
    <div class="cover__moon"></div>
    <div class="brand">
      <span class="brand__dot"></span>
      <span class="brand__name">QUILL RIDGE ACRES</span>
    </div>
  </section>

</body>
</html>
```